Maple Crest

We have opened new business that includes pottery & chimineas we want cards to have collage of pictures of products on front of card then information on back. On back in middle MAPLE CREST +
marla_fenwick@quillmail.net
(555) 218-0347
(555)2180392 & maplecrest@quillmail.net
Industry/Entity Type
Business
Font styles to use
Sans Serif
Decorative

```html
<!DOCTYPE html>
<html lang="en">
<head>
<meta charset="utf-8">
<title>Maple Crest – Business Card Back</title>
<link rel="stylesheet" href="https://fonts.googleapis.com/css2?family=Cinzel:wght@700&family=Josefin+Sans:wght@200;300&display=swap">
<style>
  :root {
    --card-bg: #050606;
    --ink: #ffffff;
  }
  html, body {
    margin: 0;
    padding: 0;
    overflow: hidden;
    background: var(--card-bg);
  }
  .card {
    position: relative;
    width: 1200px;
    height: 796px;
    background: var(--card-bg);
    color: var(--ink);
    overflow: hidden;
  }
  .card__line {
    position: absolute;
    left: 0;
    width: 100%;
    text-align: center;
    white-space: nowrap;
    margin: 0;
    line-height: 1;
  }
  .business-name {
    top: 72px;
    font-family: "Cinzel", "Times New Roman", serif;
    font-weight: 700;
    font-size: 84px;
    letter-spacing: 6px;
  }
  .owners {
    top: 212px;
    font-family: "Josefin Sans", "Helvetica Neue", sans-serif;
    font-weight: 200;
    font-size: 98px;
    letter-spacing: 3px;
  }
  .phones {
    top: 366px;
    font-family: "Josefin Sans", "Helvetica Neue", sans-serif;
    font-weight: 300;
    font-size: 52px;
  }
  .email {
    font-family: "Josefin Sans", "Helvetica Neue", sans-serif;
    font-weight: 300;
    font-size: 49px;
  }
  .email--personal { top: 450px; }
  .email--business { top: 532px; }
  .brand-mark {
    position: absolute;
    top: 652px;
    left: 0;
    width: 100%;
    display: flex;
    justify-content: center;
    align-items: center;
    gap: 14px;
  }
  .brand-mark__name {
    font-family: "Josefin Sans", "Helvetica Neue", sans-serif;
    font-weight: 300;
    font-size: 34px;
    line-height: 1;
    padding-top: 6px;
  }
</style>
</head>
<body>
  <main class="card">
    <h1 class="card__line business-name">MAPLE CREST +</h1>
    <p class="card__line owners">Dale &amp; Marla Fenwick</p>
    <p class="card__line phones">(555) 218-0347 | (555) 218-0392</p>
    <p class="card__line email email--personal">marla_fenwick@quillmail.net</p>
    <p class="card__line email email--business">maplecrest@quillmail.net</p>
    <div class="brand-mark">
      <svg class="brand-mark__dot" width="40" height="40" viewBox="0 0 40 40" aria-hidden="true">
        <circle cx="20" cy="20" r="17" fill="none" stroke="#ffffff" stroke-width="3"/>
      </svg>
      <span class="brand-mark__name">Maple Crest</span>
    </div>
  </main>
</body>
</html>
```